Marlow Air Services E-mail Signature

Need to create an email signature for Marlow Air Services. Signature should include the Marlow logo and the associated TRFC member logo

```html
<!DOCTYPE html>
<html lang="en">
<head>
<meta charset="utf-8">
<title>Marlow Air Services – E-mail Signature</title>
<link rel="stylesheet" href="https://fonts.googleapis.com/css2?family=Montserrat:wght@400;500;600;700&family=Josefin+Sans:wght@600&display=swap">
<style>
  :root {
    --backdrop: #c2c2c2;
    --paper: #ffffff;
    --brand-blue: #0062b1;
    --brand-green: #0a9a48;
    --ink: #222222;
    --ink-soft: #3a3a3a;
  }
  * { box-sizing: border-box; margin: 0; padding: 0; }
  html, body { width: 1200px; height: 1200px; overflow: hidden; background: var(--backdrop); }
  body { font-family: "Montserrat", sans-serif; color: var(--ink); }

  .canvas { position: relative; width: 1200px; height: 1200px; background: var(--backdrop); }

  .signature { position: absolute; left: 0; top: 373px; width: 1200px; height: 445px; background: var(--paper); }
  .signature__topbar { position: absolute; left: 0; top: 0; width: 100%; height: 22px; background: var(--brand-blue); }

  .brand { position: absolute; left: 60px; top: 105px; color: var(--brand-blue); font-weight: 700; line-height: 1; }
  .brand__name { display: block; font-size: 56px; letter-spacing: 1px; }
  .brand__sub { display: block; font-size: 19px; letter-spacing: 1.6px; margin-top: 6px; }

  .save-contact {
    position: absolute; left: 71px; top: 257px; width: 281px; height: 36px;
    border: 1.5px solid #333; border-radius: 8px;
    background: linear-gradient(#ffffff, #ececec);
    display: flex; align-items: center; gap: 18px; padding-left: 8px;
    font-size: 18px; font-weight: 600; letter-spacing: 1.2px; color: var(--ink);
  }
  .save-contact__mark { width: 24px; height: 24px; background: var(--brand-blue); border-radius: 2px; }

  .divider { position: absolute; left: 464px; top: 67px; width: 5px; height: 224px; background: var(--brand-blue); }

  .person { position: absolute; left: 536px; top: 70px; font-size: 35px; font-weight: 700; line-height: 1; white-space: nowrap; }
  .person__name { color: var(--brand-blue); }
  .person__sep { color: var(--brand-blue); font-weight: 500; margin: 0 26px 0 30px; }
  .person__role { color: var(--brand-green); font-weight: 600; }

  .contact { position: absolute; display: flex; align-items: flex-start; font-size: 26px; font-weight: 400; color: var(--ink-soft); line-height: 40px; white-space: nowrap; }
  .contact svg { flex: none; }
  .contact--email { left: 531px; top: 160px; }
  .contact--email svg { margin: 5px 17px 0 0; }
  .contact--address { left: 536px; top: 238px; }
  .contact--address svg { margin: 2px 20px 0 0; }
  .contact--address .contact__lines span:last-child { display: block; margin-left: -4px; }
  .contact--phone { left: 910px; top: 162px; }
  .contact--phone svg { margin: 0 20px 0 0; }
  .contact--fax { left: 909px; top: 246px; }
  .contact--fax svg { margin: 2px 16px 0 0; }

  .footer-band { position: absolute; left: 0; top: 378px; width: 887px; height: 67px; background: var(--brand-blue); display: flex; align-items: center; justify-content: center; }
  .footer-band__url { font-family: "Josefin Sans", sans-serif; font-weight: 600; font-size: 35px; color: #ffffff; padding-left: 0; margin-left: -30px; margin-top: 6px; letter-spacing: 0.5px; }

  .membership { position: absolute; left: 917px; top: 375px; }
  .membership__label { position: absolute; left: 77px; top: 6px; font-size: 15px; font-weight: 500; white-space: nowrap; color: #111; }
  .membership__mark { position: absolute; left: 1px; top: 25px; width: 60px; height: 42px; border-radius: 50%; background: var(--brand-blue); }
  .membership__name { position: absolute; left: 77px; top: 23px; font-size: 40px; font-weight: 500; letter-spacing: 3px; line-height: 1; color: #111; }
</style>
</head>
<body>
<main class="canvas">
  <section class="signature" aria-label="Marlow Air Services e-mail signature">
    <div class="signature__topbar"></div>

    <div class="brand">
      <span class="brand__name">MARLOW</span>
      <span class="brand__sub">AIR SERVICES</span>
    </div>

    <div class="save-contact">
      <span class="save-contact__mark"></span>
      <span>save to my contacts</span>
    </div>

    <div class="divider"></div>

    <h1 class="person">
      <span class="person__name">John Doe</span><span class="person__sep">|</span><span class="person__role">CEO</span>
    </h1>

    <div class="contact contact--email">
      <svg width="44" height="29" viewBox="0 0 44 29" aria-hidden="true">
        <rect width="44" height="29" fill="var(--brand-green)"/>
        <path d="M2 2 L22 18 L42 2" fill="none" stroke="#fff" stroke-width="3"/>
      </svg>
      <span>email@name.com</span>
    </div>

    <div class="contact contact--address">
      <svg width="26" height="41" viewBox="0 0 26 41" aria-hidden="true">
        <path d="M13 0 C5.8 0 0 5.8 0 13 C0 22 13 41 13 41 C13 41 26 22 26 13 C26 5.8 20.2 0 13 0 Z" fill="var(--brand-green)"/>
        <circle cx="13" cy="12.5" r="5.5" fill="#fff"/>
      </svg>
      <div class="contact__lines">
        <span>street adress here</span>
        <span>neu yrk sity. 00000</span>
      </div>
    </div>

    <div class="contact contact--phone">
      <svg width="38" height="40" viewBox="0 0 38 40" aria-hidden="true">
        <path d="M8 3 L13 10 C14 12 13 13 11 15 C13 21 17 26 22 29 C24 27 25 26 27 27 L33 32 C34 33 34 35 32 37 C29 40 25 40 20 37 C11 31 5 23 2 14 C0 9 2 5 5 3 C6 2 7 2 8 3 Z" fill="var(--brand-green)"/>
        <path d="M20 11 A8 8 0 0 1 27 18" fill="none" stroke="var(--brand-green)" stroke-width="2.5" stroke-linecap="round"/>
        <path d="M21 5 A14 14 0 0 1 33 17" fill="none" stroke="var(--brand-green)" stroke-width="2.5" stroke-linecap="round"/>
      </svg>
      <span>000 111 222 333</span>
    </div>

    <div class="contact contact--fax">
      <svg width="42" height="38" viewBox="0 0 42 38" aria-hidden="true" fill="none" stroke="var(--brand-green)" stroke-width="2.2" stroke-linejoin="round">
        <path d="M10 12 V2 H27 L32 7 V12"/>
        <rect x="2" y="12" width="38" height="18" rx="4"/>
        <rect x="10" y="22" width="22" height="15"/>
        <line x1="14" y1="27" x2="28" y2="27"/>
        <line x1="14" y1="31" x2="28" y2="31"/>
        <circle cx="8" cy="18" r="1.6" fill="var(--brand-green)" stroke="none"/>
      </svg>
      <span>000 111 222 333</span>
    </div>

    <div class="footer-band">
      <span class="footer-band__url">www.yourwebsite.com</span>
    </div>

    <div class="membership">
      <span class="membership__label">member of</span>
      <span class="membership__mark"></span>
      <span class="membership__name">TRFC</span>
    </div>
  </section>
</main>
</body>
</html>
```